Business Card Design Project - The Kernel Harbor

Company Name - The Kernel Harbor

We need a unique logo and business cards

We are a team of experienced IT professionals who specialize in providing business value to organizations via the analysis and understanding the challenges of your particular organization. We focus on understanding the challenges first, and execute against your priorities partnering with your highly valued key resources.

Our extensive experience and focus on Agile delivery methodologies help our clients continuously improve and deliver quality solutions. Using this approach we will always deliver the greatest return on your investments.

Target Market(s)

Large organizations IT departments

Industry/Entity Type

Business

Font styles to use
Serif
Sans Serif

Requirements
Should not have
• no pictures

```html
<!DOCTYPE html>
<html lang="en">
<head>
<meta charset="utf-8">
<title>The Kernel Harbor – Business Card</title>
<link rel="stylesheet" href="https://fonts.googleapis.com/css2?family=Michroma&display=swap">
<style>
  :root {
    --backdrop: #d6d8da;
    --card-white: #ffffff;
    --navy: #24358f;
    --navy-deep: #1d2c7a;
    --blue-mid: #1f6fd0;
    --cyan-glow: #0db0ec;
    --ink-light: #ffffff;
  }
  html, body {
    margin: 0;
    width: 1200px;
    height: 771px;
    overflow: hidden;
    background: var(--backdrop);
  }
  .stage {
    position: relative;
    width: 1200px;
    height: 771px;
    display: flex;
    align-items: center;
    justify-content: center;
  }
  .business-card {
    width: 840px;
    height: 480px;
    background: var(--card-white);
    box-shadow: 0 10px 30px rgba(0,0,0,0.18);
  }
  .business-card svg { display: block; }
  .brand-name {
    font-family: "Michroma", sans-serif;
    font-size: 40px;
    fill: var(--navy);
  }
  .brand-dot { fill: var(--navy); }
  .contact-line {
    font-family: "Michroma", sans-serif;
    font-size: 13px;
    fill: var(--ink-light);
    letter-spacing: 0.5px;
  }
  .contact-icon { fill: var(--ink-light); }
  .holder-name {
    font-family: "Michroma", sans-serif;
    font-size: 20px;
    fill: var(--ink-light);
    letter-spacing: 2px;
  }
  .holder-role {
    font-family: "Michroma", sans-serif;
    font-size: 13px;
    fill: var(--ink-light);
    letter-spacing: 2px;
  }
</style>
</head>
<body>
<main class="stage">
  <section class="business-card" aria-label="The Kernel Harbor business card">
    <svg width="840" height="480" viewBox="0 0 840 480" xmlns="http://www.w3.org/2000/svg">
      <defs>
        <radialGradient id="band-glow" cx="0.4" cy="0.55" r="0.75">
          <stop offset="0" stop-color="var(--cyan-glow)"/>
          <stop offset="0.45" stop-color="var(--blue-mid)"/>
          <stop offset="1" stop-color="var(--navy)"/>
        </radialGradient>
      </defs>

      <!-- brand block -->
      <circle class="brand-dot" cx="430" cy="62" r="32"/>
      <text class="brand-name" x="52" y="150">The Kernel Harbor</text>

      <!-- navy swoosh above the band -->
      <path fill="var(--navy-deep)" d="M0,178 C230,168 520,220 760,330 C540,240 260,196 0,196 Z"/>
      <!-- blue band -->
      <path fill="url(#band-glow)" d="M0,206 C270,206 560,256 840,300 L840,480 L0,480 Z"/>
      <!-- thin light line on the band edge -->
      <path fill="none" stroke="#ffffff" stroke-opacity="0.55" stroke-width="2" d="M120,210 C360,218 600,262 800,298"/>

      <!-- contact details -->
      <g class="contact-list">
        <circle class="contact-icon" cx="44" cy="244" r="6"/>
        <text class="contact-line" x="60" y="249">Suite # 418, Bay Road</text>
        <text class="contact-line" x="60" y="271">NY 10482</text>
        <circle class="contact-icon" cx="44" cy="288" r="6"/>
        <text class="contact-line" x="60" y="293">212-555-0147</text>
        <circle class="contact-icon" cx="44" cy="310" r="6"/>
        <text class="contact-line" x="60" y="315">212-555-0193</text>
        <circle class="contact-icon" cx="44" cy="332" r="6"/>
        <text class="contact-line" x="60" y="337">646-555-0128</text>
        <circle class="contact-icon" cx="44" cy="354" r="6"/>
        <text class="contact-line" x="60" y="359">hello@kernelharbor.com</text>
        <text class="contact-line" x="60" y="381">www.kernelharbor.com</text>
      </g>

      <!-- card holder -->
      <text class="holder-name" x="800" y="418" text-anchor="end">EVAN MARLOW</text>
      <text class="holder-role" x="800" y="444" text-anchor="end">OWNER / C.E.O</text>
    </svg>
  </section>
</main>
</body>
</html>
```